Postcard Design

Company Name--kinetic grove
48 Alder Row
Brooklyn New York11231
929-550-0184
www.kineticgroves-studio. example
We are a boutique personal fitness company in a exclusive neighnorhood in Brooklyn New York. We specialize in personal training and innovate new fitness classes such as Cross-Training QVM and Tabata.

We want our brand to be high-end but open to all. Laid-back but experts in the field of fitness. Innovative and flexible. Proffessional, friendly and inspiring.

Personal attention for our clients is a must as well as making sure they succeed. 87% of our clients reach their goals.

Colors should be bright but sophisticated with a little aggression but not intimidation.
Updates

Company Name-And contact info has been updated on the brief

I posted a logo. And the colors on the website have changed. If you could incorporate the website color scheme that would be helpful. If for whatever reason the logo is not here I will try to upload again.

Change the contact info: www.kineticgroves-studio.example You tube: Dorrin and the Kinetic Grove Email: Kineticgroves@kineticgroves-studio.example Verbiage changes: 'The only boutique personal fitness studio in Brooklyn. Featuring uniquely proprietary classes QVM, Cross Training and now Tabata." Verbiage Additions Safe for moms, dads and we offer enhanced childcare with certified child care development teachers with our partner studios. Classes start at $15

Please Add : Use this postcard to receive 10% any service

Hi, I could not upload the logo. However they said that our Logo should be uploaded now as I sent it to them manually.

Target Market(s)

30-40 year old women and new moms looking to do cross fit and personal training. Income 80-85K.

Industry/Entity Type

Boutique

Requirements
Must have
• Highlight Tabata and the excellence of the classes.Tag lines- Increase calorie burn by 20%. Increase muscle tone by 25%.Increase metabolism by 25%. Classes only available by appointment. 30mins or 1 hour.
Nice to have
• Attractive and fit young people having fun. Personal training.
Should not have
• Overly sexual fitness models.

```html
<!DOCTYPE html>
<html lang="en">
<head>
<meta charset="utf-8">
<title>Kinetic Grove Postcard</title>
<link href="https://fonts.googleapis.com/css2?family=Roboto+Condensed:ital,wght@0,400;0,700;0,900;1,700;1,900&display=swap" rel="stylesheet">
<style>
  :root {
    --backdrop: #5e5f61;
    --paper: #ffffff;
    --brand-red: #e8202a;
    --ink: #1c1c1c;
    --band-black: #1f1d1e;
    --accent-yellow: #ffe11a;
    --text-light: #ffffff;
    --photo-light: #f1ede9;
    --photo-mid: #d8b59c;
    --photo-dark: #3a2c26;
  }
  * { box-sizing: border-box; margin: 0; padding: 0; }
  html, body {
    width: 1200px; height: 962px; overflow: hidden;
    background: var(--backdrop);
    font-family: "Roboto Condensed", "Arial Narrow", sans-serif;
  }
  .postcard {
    position: absolute; left: 50px; top: 71px;
    width: 1100px; height: 820px;
    background: var(--paper);
    overflow: hidden;
  }
  .brand-name {
    position: absolute; left: 48px; top: 70px;
    font-size: 66px; font-weight: 700; letter-spacing: 3px;
    color: var(--ink); text-transform: uppercase; line-height: 1;
    white-space: nowrap;
  }
  .offer-panel {
    position: absolute; left: 40px; top: 210px;
    width: 1010px; height: 365px;
    background: var(--brand-red);
    border-top-right-radius: 18px;
  }
  .action-band {
    position: absolute; left: 40px; top: 575px;
    width: 1010px; height: 105px;
    background: var(--band-black);
  }
  .hero-photo {
    position: absolute; left: 680px; top: 20px;
    width: 350px; height: 660px;
    background: linear-gradient(160deg, var(--photo-dark) 0%, var(--photo-mid) 35%, var(--photo-light) 75%);
    border-radius: 175px 175px 0 0;
  }
  .intro {
    position: absolute; left: 75px; top: 228px;
    color: var(--text-light); font-weight: 700; font-size: 24px; line-height: 1.2;
    white-space: nowrap;
  }
  .classes {
    position: absolute; left: 75px; top: 300px;
    color: var(--text-light); font-weight: 900; text-transform: uppercase; line-height: 1;
    white-space: nowrap;
  }
  .classes-list { font-size: 50px; letter-spacing: -0.5px; }
  .classes-new { display: flex; align-items: flex-end; gap: 18px; margin-top: 4px; }
  .classes-now { font-size: 42px; padding-bottom: 22px; }
  .classes-feature { font-size: 96px; letter-spacing: -1px; }
  .childcare {
    position: absolute; left: 78px; top: 472px; width: 540px;
    color: var(--ink); font-size: 21px; line-height: 1.2; font-weight: 400;
  }
  .register {
    position: absolute; left: 90px; top: 592px;
    color: var(--text-light); font-size: 38px; font-weight: 900; font-style: italic;
    text-transform: uppercase; line-height: 1; white-space: nowrap;
  }
  .contact {
    position: absolute; left: 92px; top: 640px;
    display: flex; gap: 22px; white-space: nowrap;
    color: var(--accent-yellow); font-size: 22px; font-weight: 900; font-style: italic;
    text-transform: uppercase;
  }
  .price-badge {
    position: absolute; left: 830px; top: 540px;
    width: 210px; height: 210px; border-radius: 50%;
    background: var(--brand-red); border: 8px solid var(--paper);
    display: flex; flex-direction: column; align-items: center; justify-content: center;
    color: var(--text-light); font-weight: 900; text-transform: uppercase; text-align: center;
  }
  .price-label { font-size: 30px; line-height: 1; }
  .price-amount { font-size: 78px; line-height: 0.95; color: var(--accent-yellow); }
  .price-amount sup { font-size: 40px; vertical-align: 26px; }
  .discount {
    position: absolute; left: 80px; top: 720px;
    color: var(--ink); font-size: 25px; text-transform: uppercase; white-space: nowrap;
  }
  .discount strong { color: var(--brand-red); font-weight: 900; }
</style>
</head>
<body>
  <main class="postcard">
    <div class="brand-name">Kinetic Grove</div>

    <div class="offer-panel"></div>
    <div class="action-band"></div>
    <div class="hero-photo" role="img" aria-label="Photo of a smiling woman in a white tank top lifting a dumbbell"></div>

    <p class="intro">The only boutique personal fitness studio in Brooklyn.<br>Featuring uniquely proprietary classes</p>

    <div class="classes">
      <div class="classes-list">QVM, Cross Training</div>
      <div class="classes-new">
        <span class="classes-now">&amp; Now</span>
        <span class="classes-feature">Tabata</span>
      </div>
    </div>

    <p class="childcare">Safe for moms, dads and we offer enhanced childcare with certified child care development teachers with our partner studios.</p>

    <div class="register">Register Today!!</div>
    <div class="contact">
      <span class="contact-phone">929-550-0184</span>
      <span class="contact-web">www.kineticgroves-studio.example</span>
    </div>

    <div class="price-badge">
      <span class="price-label">Classes<br>start at</span>
      <span class="price-amount"><sup>$</sup>15</span>
    </div>

    <p class="discount">Use this postcard to receive <strong>10% off</strong> on any service</p>
  </main>
</body>
</html>
```